Client Publishing Agency Brochure

We need a company brochure for a new company based in Cape Town, South Africa called Velvet Harbour Studios (VHS).

We need a brochure marketing our publishing agency (vhs:inkwell) and our creative, interactive & print production division (vhs:forge). Develop a fresh design concept which will direct the design of our new website in the near future. (So don't pay attention to our current web page. It does not reflect our brand).

vhs:inkwell is a content marketing agency offering our clients (B2B, B2C, NPO, Professional & Membership Organizations) branded publishing to build trust, authority and relationships with their customers. A typical content strategy may include communication through client print or online magazine, newsletters, microsite, website, social technology and plenty more). We want to communicate that company's need to change their mind set from promoting their products and begin to invest in developing a relationship with their potential & existing customers. The drive is a Return On Objectives (business & marketing objectives) and interest is a Return On Investment (ROI).

vhs:forge is a creative, interactive & print production agency which supports our client's marketing collateral needs.
Updates

Hi Designers,

This is a response to questions posted earlier to assist you in your project.

Q.What will the size of brochure be?
A. A4 size with folder flap for the back cover

Q.Will it be a three panels double sided?
A. Depends on your creative concept. But if you make a 3 panel dbl side then layout two version for print (double sided 3 panel) and digital pdf (single pdf pages in sequence).

Q.The images that you supplied I know are just samples, What type of images are 
required? 
A. Depends on your creative concept. Let the style of the logo inspire you. What I liked in the examples is the classic, premium, quality feel. So no business stock imagery. I'm also a creative agency so that message needs to come through. Illustrated styles are welcome.

Q.Should design have same feel as your website? 
A. No. Our website is pending the outcome of the brochure. The brochure will be our creative direction for our new website. So creative an inspiring and clean brochure.

Please feel free to post additional questions. Good Luck and thank you for your participation.

Project Deadline Extended
Reason: The designers have not produced a style and concept that reflects our brand. Would like to guide them more to reach the right look for our company.

Hi Designers...

I have not been happy with the quality of ideas and execution of those ideas. This I understand could a combination of a poor brief and a non-guarenteed project.

I have rectified the brief and have guaranteed the award. Please don't hold back on your creativity and return the guarantee for high quality.

Please ask me any questions to better understand what we are looking for.

Remember. This brochure is a new design concept. Do not visit the web page for inspiration. The new design concept for the brochure will set the tone and inspire a new website.

Lets create a beautiful product together.

Thank you for your participation.

Project Deadline Extended
Reason: Designers are not following the brief, and not respecting the logo and colour policies/guidelines and those who are submitting work are not asking questions throughout the process to get a better understanding of what we need. All design submissions are always at the last minute. And some designers are are not real designers and using web development software to produce print designs. More importantly after taking time to advise designers of changes, no effort is made by designers to make changes. Each designer submits 1 idea and think that they are going to win the lottery. Where is the work ethic and quality of service? Where are the submissions from the designers who accepted the participation fee? There were a few designers who promised participation and never showed up. Maybe it all our fault? But we not happy with the service and level of creativity. Not sure if these designers are taking pride in their work or not. I know a few of you are.

Target Market(s)

B2B, B2C, NPO, Professional & Membership Organizations - Make up professionals and decision makers across sectors from Shipping and Logistics, Manufacturing, Legal to Art & Culture.

Industry/Entity Type

Communication

Requirements
Must have
• Size: A4
x 2 Panels
+ Folder flap (for A4 Paper, business card slot)
Styled map to our premises. See map attachment for example.

Pages: 10 including cover (if you need more than this let your design motivate the need for more pages)

(See logo use eps file)
(See colour use eps file)

Nice to have
• Styled map to our premises. See attachment for example.
Should not have
• Do not take any inspiration from our website. It is just a free template to show customers that it is still under construction.

Do not include stock symbols and typical business stock images. Remember we are a creative offering, so our brochure should show originality, innovation and individuality.

```html
<!DOCTYPE html>
<html lang="en">
<head>
<meta charset="utf-8">
<title>VHS inkwell – Our Approach</title>
<link rel="stylesheet" href="https://fonts.googleapis.com/css2?family=Roboto:wght@300;400&display=swap">
<style>
  :root {
    --backdrop: #ebebeb;
    --paper: #ffffff;
    --brand-red: #d51a3b;
    --pattern-red: #e4566e;
    --sky-blue: #5ec3ea;
    --ink: #2b2b2b;
    --white: #ffffff;
  }
  * { margin: 0; padding: 0; box-sizing: border-box; }
  html, body {
    width: 1200px; height: 900px; overflow: hidden;
    background: var(--backdrop);
    font-family: "Roboto", Arial, sans-serif;
  }
  .spread {
    position: absolute; left: 72px; top: 40px;
    width: 1072px; height: 776px;
    filter: drop-shadow(0 4px 8px rgba(0,0,0,0.18));
  }
  .page { position: absolute; top: 0; height: 100%; overflow: hidden; }
  .page--left {
    left: 0; width: 540px;
    background: var(--paper);
    border-top-left-radius: 110px 150px;
  }
  .page--right {
    left: 540px; width: 532px;
    background: var(--brand-red);
    border-top-right-radius: 64px 80px;
  }

  .intro {
    position: absolute; left: 274px; top: 40px; width: 256px;
    color: var(--brand-red); font-size: 12px; line-height: 16.6px;
  }
  .brand-name {
    position: absolute; left: 28px; top: 372px;
    color: var(--ink); font-size: 22px; line-height: 26px; font-weight: 400;
    white-space: nowrap;
  }
  .objectives-heading {
    position: absolute; left: 274px; top: 264px; width: 244px;
    color: var(--brand-red); font-size: 28px; line-height: 27px; font-weight: 300;
  }
  .objectives-text {
    position: absolute; left: 274px; top: 452px; width: 248px;
    color: var(--sky-blue); font-size: 12px; line-height: 16.6px;
  }
  .closing-title {
    position: absolute; left: 22px; bottom: 4px;
    color: var(--brand-red); font-size: 57px; line-height: 60px; font-weight: 300;
    white-space: nowrap;
  }

  .corner-pattern {
    position: absolute; left: 308px; top: 0; width: 224px; height: 112px;
    background: linear-gradient(200deg, var(--pattern-red), var(--brand-red));
  }
  .approach-title {
    position: absolute; left: 48px; top: 236px;
    color: var(--sky-blue); font-size: 74px; line-height: 74px; font-weight: 300;
    white-space: nowrap;
  }
  .column {
    position: absolute; top: 334px;
    color: var(--white); font-size: 10px; line-height: 12.2px;
  }
  .column p + p { margin-top: 12.2px; }
  .column--first { left: 54px; width: 222px; }
  .column--second { left: 314px; width: 200px; }
  .column .highlight { color: var(--sky-blue); margin-top: 16px; }
</style>
</head>
<body>
  <div class="spread">
    <section class="page page--left">
      <p class="intro">VHS inkwell will help you ignite meaningful conversations with your community to build trust, authority and profitable engagement. We are experts in creating compelling original communication that advocates, motivates sharing and drives business. The result of consistent engagement with your customers through the right set of media (print or digital) is a return on marketing &amp; business objectives (ROO). Our premium client magazine, e-zines, newsletters, microsite, website, animation, corporate videos and organic seo solutions deliver ROO for ROI.</p>

      <p class="brand-name">Velvet Harbour Studios</p>

      <h2 class="objectives-heading">Objectives that drive your business – achieved through authentic content engagement</h2>

      <p class="objectives-text">Your brand and organization may use our content services as a means of achieving a variety of business objectives, such as product extension, thought leadership, lead generation, increasing direct sales, referrals, improving retention, improving a negative image and much more.</p>

      <h1 class="closing-title">VHS: inkwell engage</h1>
    </section>

    <section class="page page--right">
      <div class="corner-pattern" role="img" aria-label="Decorative lattice of white diamonds in the top corner"></div>

      <h2 class="approach-title">Our Approach</h2>

      <div class="column column--first">
        <p>Shouting out your brand virtues is the old marketer's approach. This type of communication uses marketing collateral (brochures, event marketing material, advertising). Customers care less about how special you are and care more for the relevant difference you make in their lives and business. Finding a single opportunity of making a difference is only achieved through consistent meaningful conversations about the interests, issues, and opportunities that matter the most to your audience. It's the art of conversation and engagement versus talking to your valued clients. This type of communication is achieved through content marketing strategies (client magazine, e-zines, newsletters, microsite, website, social technology and plenty more).</p>
        <p>We create fine editorial combined with steel quality photography that sparks conversations within your community and continuously connect to motivate them to share your strategic message with their extended networks.</p>
      </div>

      <div class="column column--second">
        <p>When you begin understanding your clients, whether they are internal (employees) or external, you'll find an opportunity for your brand to be reinforced as a trusted partner. Trust is the currency your brand should be investing in. Return on Objectives should be your primary success indicator followed by sales. Sustainable relationships will deliver Return on Investment shared with your customers.</p>
        <p class="highlight">We deliver well-crafted editorial and web content at the point where traditional marketing collateral strategy meets new aged content engineering. It's about bringing real value to your readers while maximizing your marketing and business objectives effectively. It's about bringing real value to your readers while maximizing your marketing and business objectives effectively.</p>
      </div>
    </section>
  </div>
</body>
</html>
```